Business Cards for our company

Hi there,

we have successfully designed a logo with ArtFlock and would like now to design our business cards. We would like to keep the colours and the look-and-feel of the logo. Please send in variations with two or three colours and one or two sides. I promise to respond to every single submission.

Many thanks and happy new year.

All the best,
Wilfried

Target Market(s)

B2B

Industry/Entity Type

Trade

Contact Information for Business Card

We have successfully designed a logo with ArtFlock and would like now to design our business cards. We would like to keep the colours and the look-and-feel of the logo. Please send in variations with two or three colours and one or two sides. I promise to respond to every single submission.

Font styles to use
Serif
Sans Serif
Script

Requirements
Must have
• These information should be on the business card, grouped as you suggest, and we think using small pictograms for mobile, email, etc is pretty helpful:
• Wilfried Tammler (first and second name)
• Geschäftsführer/ Managing Director (title)
• KoR Warenkontor GmbH (company name and legal form)
• Ostheimer Str. 18/3 (street and house number)
• 71463 Lindenau (zip code and town)
• +491709384562 (mobile)
• +4971569027341 (work)
• w.tammler@kor-warenkontor.example (email)
• www.kor-warenkontor.example (web)
Nice to have
• Spectacular and interesting layout and design. You look at it and think, wow, that's not the normal stuff.
• We think of ourselves as bridge-builders between businesses (international producers on the one hand, and retail chains on the other hand) and we translate, organise and manage projects where both partners are involved, but it's difficult for them to cooperate due to language barriers and different working cultures.
• This is why we have the n between the B's shaped as a bridge, and the green arc supports this idea. Maybe you could play with this idea...
Should not have
• the standard layout that everybody has

```html
<!DOCTYPE html>
<html lang="de">
<head>
<meta charset="utf-8">
<title>KoR Warenkontor – Visitenkarte</title>
<link rel="stylesheet" href="https://fonts.googleapis.com/css2?family=Cinzel:wght@400;600;700&display=swap">
<style>
  :root {
    --green: #2fae48;
    --black: #0b0b0b;
    --white: #ffffff;
    --ink: #1a1a1a;
    --backdrop: #d9dbd9;
  }
  * { margin: 0; padding: 0; box-sizing: border-box; }
  html, body { width: 1200px; height: 947px; overflow: hidden; }
  body {
    background: var(--backdrop);
    font-family: "Cinzel", serif;
    position: relative;
  }
  .card {
    position: absolute;
    top: 323px;
    width: 520px;
    height: 300px;
    border-radius: 56px 0 56px 0;
    overflow: hidden;
    box-shadow: 0 10px 28px rgba(0,0,0,.18);
  }
  /* Front side */
  .card-front { left: 50px; background: var(--white); color: var(--ink); }
  .dot { position: absolute; border-radius: 50%; background: var(--green); }
  .dot-small { width: 30px; height: 30px; left: 40px; top: 24px; }
  .dot-large { width: 52px; height: 52px; left: 150px; top: 82px; }
  .rule-top {
    position: absolute; left: 108px; right: 0; top: 42px;
    height: 2px; background: var(--green);
  }
  .contact {
    position: absolute; right: 28px; top: 98px;
    text-align: right; font-size: 13px; line-height: 1.4;
  }
  .contact .name {
    color: var(--green); font-size: 23px; font-weight: 600;
    letter-spacing: .5px; line-height: 1.15;
  }
  .contact .title {
    display: inline-block; font-size: 12px;
    border-top: 1px solid var(--ink); padding: 2px 0 0 40px; margin-bottom: 14px;
  }
  .contact .row { display: flex; justify-content: flex-end; align-items: center; gap: 6px; }
  .contact .row svg { width: 15px; height: 15px; flex: none; }
  .contact .address { margin-bottom: 4px; }
  .front-brand {
    position: absolute; left: 34px; bottom: 40px;
    display: flex; align-items: center; gap: 10px;
    font-size: 36px; font-weight: 700; color: var(--black);
  }
  .front-brand .mark { width: 20px; height: 20px; background: var(--green); border-radius: 50%; }
  /* Back side */
  .card-back { left: 630px; background: var(--black); }
  .band { position: absolute; left: 0; right: 0; height: 12px; background: var(--green); }
  .band-top { top: 0; }
  .band-bottom { bottom: 62px; }
  .back-brand {
    position: absolute; left: 0; right: 0; top: 96px;
    text-align: center; color: var(--white);
    font-size: 38px; font-weight: 700; letter-spacing: 1px; line-height: 1.1;
  }
</style>
</head>
<body>
  <section class="card card-front" aria-label="Vorderseite">
    <span class="dot dot-small"></span>
    <span class="rule-top"></span>
    <span class="dot dot-large"></span>

    <div class="front-brand"><span class="mark"></span>KoR</div>

    <div class="contact">
      <div class="name">Wilfried Tammler</div>
      <div class="title">Geschäftsführer</div>
      <div class="address">Ostheimer Str. 18/3<br>71463 Lindenau</div>
      <div class="row">+491709384562
        <svg viewBox="0 0 16 16"><circle cx="8" cy="8" r="8" fill="var(--green)"/><rect x="5.5" y="3.5" width="5" height="9" rx="1" fill="none" stroke="#fff" stroke-width="1.2"/></svg>
      </div>
      <div class="row">+4971569027341
        <svg viewBox="0 0 16 16"><circle cx="8" cy="8" r="8" fill="var(--green)"/><path d="M5 4.5c0 4 2.5 6.5 6.5 7l.8-1.6-1.8-1-1 .9c-1.3-.6-2.2-1.5-2.8-2.8l.9-1-1-1.8z" fill="#fff"/></svg>
      </div>
      <div class="row">w.tammler@kor-warenkontor.example
        <svg viewBox="0 0 16 16"><circle cx="8" cy="8" r="8" fill="var(--green)"/><rect x="4" y="5" width="8" height="6" fill="#fff"/><path d="M4 5l4 3.2L12 5" fill="none" stroke="var(--green)" stroke-width="1"/></svg>
      </div>
      <div class="row">www.kor-warenkontor.example
        <svg viewBox="0 0 16 16"><circle cx="8" cy="8" r="8" fill="var(--green)"/><g fill="none" stroke="#fff" stroke-width="1"><circle cx="8" cy="8" r="4.5"/><ellipse cx="8" cy="8" rx="2" ry="4.5"/><path d="M3.5 8h9"/></g></svg>
      </div>
    </div>
  </section>

  <section class="card card-back" aria-label="Rückseite">
    <span class="band band-top"></span>
    <div class="back-brand">KoR<br>Warenkontor</div>
    <span class="band band-bottom"></span>
  </section>
</body>
</html>
```